KelvrasMassage website required

We need a website for a mobile sports massage therapist in the United Kingdom. Specialising in pregnancy and postnatal massage, sports and remedial, deep tissue massage & Corprate Massage. Attached are some logos that we already have in various colours. The file named logo_white_background is what we normally use. Feel free to use the others at your discretion.

Requirements
Must have
• Service areas, Booking system.

```html
<!DOCTYPE html>
<html lang="en">
<head>
<meta charset="utf-8">
<title>Kelvra's Massage</title>
<link href="https://fonts.googleapis.com/css2?family=Open+Sans:wght@300;400;600;700&display=swap" rel="stylesheet">
<style>
  :root {
    --white: #ffffff;
    --ink-soft: #7a7a7a;
    --ink-text: #8a8a8a;
    --rule: #8f8f8f;
    --accent: #6cc6e8;
    --band-left: #4d7393;
    --band-right: #1d3c5c;
  }
  * { margin: 0; padding: 0; box-sizing: border-box; }
  html, body { width: 1200px; height: 1200px; overflow: hidden; background: var(--white); }
  body { position: relative; font-family: 'Open Sans', sans-serif; }

  .hero-photo { position: absolute; left: 0; top: 0; width: 1200px; height: 640px; }

  .brand {
    position: absolute; left: 120px; top: 34px;
    color: var(--white); font-weight: 600; font-size: 17px;
    line-height: 1.3; letter-spacing: 2px; text-transform: uppercase;
  }

  .main-nav { position: absolute; top: 60px; left: 0; width: 1200px; height: 24px; }
  .main-nav a {
    position: absolute; transform: translateX(-50%);
    color: var(--white); text-decoration: none; font-size: 16px;
    font-weight: 400; white-space: nowrap; letter-spacing: 0.2px;
  }

  .hero-title {
    position: absolute; left: 366px; top: 173px; width: 468px; height: 168px;
    border-top: 1px solid rgba(255,255,255,0.45);
    border-bottom: 1px solid rgba(255,255,255,0.45);
    color: var(--white); text-align: center; font-weight: 700;
  }
  .hero-title .name-line { display: block; font-size: 54px; line-height: 1; margin-top: 28px; }
  .hero-title .name-sub { display: block; font-size: 30px; letter-spacing: 18px; margin-top: 20px; padding-left: 18px; }

  .hero-service-areas {
    position: absolute; left: 360px; top: 366px; width: 480px;
    color: var(--white); text-align: center; font-size: 22.4px; line-height: 33px;
  }

  .slider-arrow { position: absolute; top: 212px; width: 12px; height: 18px; }
  .slider-arrow.prev { left: 110px; }
  .slider-arrow.next { left: 1081px; }

  .notch { position: absolute; width: 44px; height: 44px; margin-left: -22px; margin-top: -22px; }

  .welcome { position: absolute; left: 0; top: 667px; width: 1200px; text-align: center; }
  .welcome .rule { width: 116px; height: 1px; background: var(--rule); margin: 0 auto; }
  .welcome h1 { font-weight: 400; font-size: 38px; color: var(--ink-soft); margin-top: 20px; line-height: 48px; }
  .welcome p { font-size: 14.6px; line-height: 24.3px; color: var(--ink-text); margin-top: 26px; }
  .book-now {
    display: inline-block; margin-top: 30px; width: 136px; height: 40px;
    border: 1px solid var(--accent); color: var(--accent); font-weight: 600;
    font-size: 16px; line-height: 38px; text-decoration: none;
  }

  .feature-band { position: absolute; left: 0; top: 1039px; width: 1200px; height: 161px; display: flex; }
  .feature-band .tile { height: 100%; }
  .feature-band .tile.left { width: 598px; background: linear-gradient(90deg, #4a6f8e, #5a7f9e 50%, #3f6483); }
  .feature-band .tile.right { width: 602px; background: linear-gradient(90deg, #2a4a6a, var(--band-right)); }
</style>
</head>
<body>

<svg class="hero-photo" viewBox="0 0 1200 640" role="img" aria-label="Photo of a woman receiving a hot stone back massage in a dim spa room">
  <defs>
    <linearGradient id="heroTone" x1="0" y1="0" x2="1" y2="1">
      <stop offset="0" stop-color="#2a1c14"/>
      <stop offset="0.35" stop-color="#6a4424"/>
      <stop offset="0.6" stop-color="#7a5234"/>
      <stop offset="1" stop-color="#2a1a12"/>
    </linearGradient>
    <linearGradient id="heroShade" x1="0" y1="0" x2="0" y2="1">
      <stop offset="0" stop-color="#000" stop-opacity="0.75"/>
      <stop offset="0.45" stop-color="#000" stop-opacity="0.25"/>
      <stop offset="1" stop-color="#000" stop-opacity="0.35"/>
    </linearGradient>
  </defs>
  <path d="M0 0 H1200 V156 L1108 540 Q1082 640 990 634 L0 346 Z" fill="url(#heroTone)"/>
  <path d="M0 0 H1200 V156 L1108 540 Q1082 640 990 634 L0 346 Z" fill="url(#heroShade)"/>
</svg>

<div class="brand">Kelvra's<br>Massage</div>

<nav class="main-nav">
  <a href="#" style="left:546px">HOME</a>
  <a href="#" style="left:665px">ABOUT US</a>
  <a href="#" style="left:790px">SERVICE</a>
  <a href="#" style="left:910px">GALLERY</a>
  <a href="#" style="left:1039px">CONTACTS</a>
</nav>

<svg class="slider-arrow prev" viewBox="0 0 12 18" aria-label="Previous slide"><path d="M10 1 L2 9 L10 17" fill="none" stroke="#fff" stroke-width="1.3"/></svg>
<svg class="slider-arrow next" viewBox="0 0 12 18" aria-label="Next slide"><path d="M2 1 L10 9 L2 17" fill="none" stroke="#fff" stroke-width="1.3"/></svg>

<div class="hero-title">
  <span class="name-line">Kelvra's</span>
  <span class="name-sub">MASSAGE</span>
</div>

<p class="hero-service-areas">Mobile massage across Brookhaven<br>and nearby areas. Book online today.</p>

<svg class="notch" style="left:600px;top:528px" viewBox="0 0 44 44" aria-hidden="true">
  <circle cx="22" cy="22" r="22" fill="#fff"/>
  <path d="M12 19 L22 28 L32 19" fill="none" stroke="#8a8a8a" stroke-width="1.3"/>
</svg>

<section class="welcome">
  <div class="rule"></div>
  <h1>WELCOME</h1>
  <p>Mobile sports massage brought to your home, gym or office across the UK. We specialise in<br>
  pregnancy and postnatal massage, sports and remedial work, deep tissue treatment and corporate<br>
  sessions for busy teams. Choose your service area and book a time that suits you online<br>
  in minutes, with flexible morning and evening slots</p>
  <a class="book-now" href="#">Book now</a>
</section>

<div class="feature-band">
  <div class="tile left" role="img" aria-label="Photo of a therapist treating a client on a massage table, blue tint"></div>
  <div class="tile right" role="img" aria-label="Photo of a spa treatment with soft bokeh lights, deep blue tint"></div>
</div>

<svg class="notch" style="left:600px;top:1039px" viewBox="0 0 44 44" aria-hidden="true">
  <circle cx="22" cy="22" r="22" fill="#fff"/>
  <path d="M12 19 L22 28 L32 19" fill="none" stroke="#8a8a8a" stroke-width="1.3"/>
</svg>

</body>
</html>
```